Business Card Re-Design for a Lighting Designer

I would like my business card re-designed. It is currently high gloss and they scratch too easily. I don not think the current design lends itself well to a matte finish. I have included the current design for reference along with our company logo.
Check out our website for current branding.
http://www.brambleorchidstudio.example

Updates
Some of the top contenders are muslim and it is a holiday for them. I do not want to discriminate and would expect the same courtesy for holidays we celebrate.
Target Market(s)
Interior Designers, Architects
Contact Information for Business Card
Logo - Name, Title, Address, Telephone Number and Extension, Email
Font styles to use
Requirements
Must have
- All the information listed on the current business card. If you use Red, it needs to be the red from our logo.
Nice to have
- Vertical and Horizontal Designs will be entertained.
Should not have
- Requirements for a glossy finish...should not look too corporate since we are a design firm.

```html
<!DOCTYPE html>
<html lang="en">
<head>
<meta charset="utf-8">
<title>Bramble Orchid Studio — Business Card</title>
<link href="https://fonts.googleapis.com/css2?family=Roboto:wght@400;500;700&display=swap" rel="stylesheet">
<style>
  :root {
    --brand-red: #9e1016;
    --frost: #ece3da;
    --frost-edge: #f6f0ea;
    --ink: #1d1b1a;
    --muted: #8a8580;
    --paper-white: #ffffff;
    --backdrop: #e4e1dd;
  }
  * { box-sizing: border-box; margin: 0; padding: 0; }
  html, body {
    width: 1200px;
    height: 873px;
    overflow: hidden;
    background: var(--backdrop);
    font-family: "Roboto", Arial, sans-serif;
  }
  .canvas {
    width: 1200px;
    height: 873px;
    display: flex;
    align-items: center;
    justify-content: center;
  }
  .card {
    width: 660px;
    height: 600px;
    border-radius: 30px;
    overflow: hidden;
    display: flex;
    box-shadow: 0 10px 30px rgba(0,0,0,0.18);
  }
  .card__brand {
    width: 300px;
    background: linear-gradient(160deg, var(--frost-edge), var(--frost));
    display: flex;
    flex-direction: column;
    justify-content: center;
    padding: 0 34px;
  }
  .brand-lockup {
    display: flex;
    align-items: center;
    gap: 14px;
  }
  .brand-lockup__square {
    width: 30px;
    height: 30px;
    flex: none;
    background: var(--brand-red);
  }
  .brand-lockup__name {
    font-size: 30px;
    font-weight: 400;
    line-height: 1.1;
    color: var(--ink);
    text-transform: uppercase;
  }
  .brand-rule {
    margin-top: 22px;
    height: 2px;
    background: var(--brand-red);
  }
  .brand-tagline {
    margin-top: 8px;
    font-size: 13px;
    letter-spacing: 0.08em;
    color: var(--muted);
    text-transform: uppercase;
  }
  .card__contact {
    flex: 1;
    background: var(--brand-red);
    color: var(--paper-white);
    padding: 120px 36px 0 44px;
  }
  .contact-name {
    font-size: 30px;
    font-weight: 700;
    letter-spacing: 0.02em;
    text-transform: uppercase;
  }
  .contact-title {
    font-size: 17px;
    font-weight: 500;
    letter-spacing: 0.06em;
    text-transform: uppercase;
    margin-bottom: 22px;
  }
  .contact-address {
    font-size: 18px;
    line-height: 1.4;
    margin-bottom: 10px;
  }
  .contact-list { list-style: none; }
  .contact-list li {
    display: flex;
    align-items: center;
    gap: 12px;
    font-size: 18px;
    line-height: 1.55;
    white-space: nowrap;
  }
  .contact-list svg {
    width: 17px;
    height: 17px;
    flex: none;
    fill: var(--paper-white);
  }
</style>
</head>
<body>
<main class="canvas">
  <article class="card">
    <section class="card__brand">
      <div class="brand-lockup">
        <span class="brand-lockup__square"></span>
        <span class="brand-lockup__name">Bramble Orchid Studio</span>
      </div>
      <div class="brand-rule"></div>
      <p class="brand-tagline">Lighting for Architecture</p>
    </section>
    <section class="card__contact">
      <h1 class="contact-name">Maren Castellane</h1>
      <p class="contact-title">Principal</p>
      <p class="contact-address">217 Larkspur Commons STE 40<br>Fairhaven, Georgia 30999</p>
      <ul class="contact-list">
        <li>
          <svg viewBox="0 0 24 24" aria-hidden="true"><path d="M6.6 10.8a15.5 15.5 0 0 0 6.6 6.6l2.2-2.2a1 1 0 0 1 1-.25 11.4 11.4 0 0 0 3.6.57 1 1 0 0 1 1 1V20a1 1 0 0 1-1 1A17 17 0 0 1 3 4a1 1 0 0 1 1-1h3.5a1 1 0 0 1 1 1c0 1.25.2 2.45.57 3.6a1 1 0 0 1-.25 1z"/></svg>
          555.014.2290 x1
        </li>
        <li>
          <svg viewBox="0 0 24 24" aria-hidden="true"><path d="M2 5h20v14H2zm2 2v.4l8 5.2 8-5.2V7zm0 2.8V17h16V9.8l-8 5.2z"/></svg>
          maren@brambleorchidstudio.example
        </li>
        <li>
          <svg viewBox="0 0 24 24" aria-hidden="true"><path d="M12 2a10 10 0 1 0 0 20 10 10 0 0 0 0-20zm7.9 9h-3.4a15 15 0 0 0-1.4-6.2A8 8 0 0 1 19.9 11zM12 4.1c.9 1.2 2.3 3.6 2.5 6.9h-5c.2-3.3 1.6-5.7 2.5-6.9zM8.9 4.8A15 15 0 0 0 7.5 11H4.1a8 8 0 0 1 4.8-6.2zM4.1 13h3.4a15 15 0 0 0 1.4 6.2A8 8 0 0 1 4.1 13zm7.9 6.9c-.9-1.2-2.3-3.6-2.5-6.9h5c-.2 3.3-1.6 5.7-2.5 6.9zm3.1-.7a15 15 0 0 0 1.4-6.2h3.4a8 8 0 0 1-4.8 6.2z"/></svg>
          www.brambleorchidstudio.example
        </li>
      </ul>
    </section>
  </article>
</main>
</body>
</html>
```